2-4 page graphic work for a press kit

I need a press kit designed for an app. This is a very simple presentation of the app with only a little text and a few pictures that the designer can choose from and use at will. There is a word document with the text, a few pictures, screenshots of the app as well as the logo. SImply follow the order of the text and put corresponding photos if you feel they apply.
If you want to add other pictures that is fine but they must follow the same theme which is basically things that you would do with your friends; lunch, go running, go to the museum, go to the movies etc.
Work

```html
<!DOCTYPE html>
<html lang="en">
<head>
<meta charset="utf-8">
<title>Kin Loop – Press Kit</title>
<link rel="stylesheet" href="https://fonts.googleapis.com/css2?family=Open+Sans:wght@300;400;700&display=swap">
<style>
  :root {
    --mint: #e1eeed;
    --teal: #14a6b1;
    --teal-deep: #0f98a3;
    --ink: #5e6163;
    --ink-strong: #4f5254;
    --white: #ffffff;
  }
  * { margin: 0; padding: 0; box-sizing: border-box; }
  html, body { width: 927px; height: 1200px; overflow: hidden; background: var(--white); }
  .page {
    position: relative;
    width: 927px;
    height: 1200px;
    overflow: hidden;
    font-family: "Open Sans", Arial, sans-serif;
    background: var(--white);
  }
  .intro-panel {
    position: absolute;
    left: 0; top: 0;
    width: 927px; height: 520px;
  }
  .intro-text {
    position: absolute;
    left: 18px; top: 136px;
    width: 600px;
    color: var(--ink);
    font-size: 12.6px;
    line-height: 21px;
    font-weight: 400;
  }
  .intro-text p + p { margin-top: 21px; }
  .brand-inline {
    font-weight: 700;
    font-size: 17px;
    color: var(--ink-strong);
  }
  .app-mark {
    position: absolute;
    left: 715px; top: 201px;
    width: 156px; height: 156px;
    display: flex;
    flex-direction: column;
    align-items: center;
    justify-content: center;
    gap: 12px;
  }
  .app-mark__square {
    width: 96px; height: 96px;
    border-radius: 20px;
    background: var(--teal);
  }
  .app-mark__name {
    font-weight: 700;
    font-size: 20px;
    color: var(--teal);
  }
  .photo-strip {
    position: absolute;
    left: 0; top: 556px;
    width: 927px; height: 265px;
  }
  .quote-band {
    position: absolute;
    left: 0; top: 859px;
    width: 927px; height: 341px;
    background: var(--teal);
  }
  .tagline {
    position: absolute;
    right: 27px; top: 50px;
    width: 520px;
    color: var(--white);
    font-weight: 300;
    font-size: 39px;
    line-height: 57px;
    text-align: right;
  }
  .tagline__mark {
    font-family: Georgia, "Times New Roman", serif;
    font-weight: 700;
    font-size: 44px;
    line-height: 0;
    letter-spacing: -4px;
  }
  .tagline__last { display: block; padding-right: 60px; }
</style>
</head>
<body>
<main class="page">
  <svg class="intro-panel" viewBox="0 0 927 520" aria-hidden="true">
    <polygon points="0,0 323,0 623,333 485,515 0,515" fill="var(--mint)"/>
  </svg>

  <section class="intro-text">
    <p>Have you ever found yourself in the situation where you want to attend<br>
    a concert, go to an art exhibition, explore a mountain trail or simply just<br>
    try out a new café, but you have no one to come with you? Do you end up<br>
    cancelling it?</p>
    <p>After having moved moving around between different cities and countries, the<br>
    developers of <span class="brand-inline">Kin Loop</span> encountered the pitfall of a limited social network and<br>
    the difficulties of re-establishing social connections. During the period of lost<br>
    experiences and cancelled plans, the idea behind <span class="brand-inline">Kin Loop</span> came into light.</p>
  </section>

  <div class="app-mark">
    <div class="app-mark__square"></div>
    <span class="app-mark__name">Kin Loop</span>
  </div>

  <svg class="photo-strip" viewBox="0 0 927 265">
    <defs>
      <linearGradient id="beach" x1="0" y1="0" x2="0" y2="1">
        <stop offset="0" stop-color="#9fb9cf"/>
        <stop offset="0.45" stop-color="#6f8aa0"/>
        <stop offset="1" stop-color="#c9b294"/>
      </linearGradient>
      <linearGradient id="snack" x1="0" y1="0" x2="1" y2="1">
        <stop offset="0" stop-color="#d9d4cb"/>
        <stop offset="0.55" stop-color="#c59a5c"/>
        <stop offset="1" stop-color="#e8e3dc"/>
      </linearGradient>
      <linearGradient id="terrace" x1="0" y1="0" x2="0" y2="1">
        <stop offset="0" stop-color="#d8cdb8"/>
        <stop offset="0.5" stop-color="#b08a6a"/>
        <stop offset="1" stop-color="#8c7a66"/>
      </linearGradient>
    </defs>
    <polygon role="img" aria-label="Group of friends in wetsuits cheering on a beach" points="0,0 441,0 250,265 0,265" fill="url(#beach)"/>
    <polygon role="img" aria-label="Hand picking fries from a basket beside a glass of wine" points="465,0 674,0 732,265 291,265" fill="url(#snack)"/>
    <polygon role="img" aria-label="Two friends sharing lunch at a sunny outdoor table" points="715,0 927,0 927,265 745,265" fill="url(#terrace)"/>
  </svg>

  <section class="quote-band">
    <p class="tagline"><span class="tagline__mark">“</span> The app that connects you with new people and allows you to grow your <span class="tagline__last">social network <span class="tagline__mark">”</span></span></p>
  </section>
</main>
</body>
</html>
```